Garden building leaflet A4 tri fold

We need an A4 tri fold (printed both sides) flyer design for a local business based in East Hampshire (UK) called Corrick Yard Buildings.We offer a bespoke garden building service from design, construction, installation and maintenance.Typical use is for home office, garden studio, playrooms, garage workshops, therapy rooms and extra living accommodation. Including connection to all services as required.The final design should stress that this is a local business that has been serving the East Hampshire community for almost 20 years. Over this time Corrick's has built a reputation for quality construction with customer satisfaction the overriding driving force.Over the last 20 years we've seen a huge increase in people working from home at least one day per week and a shift back to family focused lifestyles. Even large multi national companies are promoting home working as it has been shown by recent studies home workers are more productive than solely office based employees. Corrick Yard Buildings is a greener way of working, improves work-life balance and accelerates your productivity.

Target Market(s)

ABC1

Industry/Entity Type

Business

Requirements
Must have
• Pictures/photos of garden office buildings and garden studios in typical UK garden surroundings. Contemporary structures essential with modern building design.
Nice to have
• Internal pictures of people working in a garden room or garden studio environment.

```html
<!DOCTYPE html>
<html lang="en">
<head>
<meta charset="utf-8">
<title>Corrick Yard Buildings – Tri-fold Leaflet</title>
<link href="https://fonts.googleapis.com/css2?family=Questrial&family=Montserrat:wght@700&display=swap" rel="stylesheet">
<style>
  :root{
    --stage:#2a2c0b;
    --paper:#ffffff;
    --lime-soft:#eef3c2;
    --lime:#c9dc3c;
    --lime-bright:#d7e84a;
    --leaf:#3f8a1f;
    --forest:#1f4d12;
    --ink:#2f2f2f;
    --phone:#e0141b;
    --rule:#b9c27a;
  }
  *{box-sizing:border-box;margin:0;padding:0}
  html,body{width:1200px;height:1000px;overflow:hidden;background:var(--stage)}
  body{position:relative;font-family:"Questrial",sans-serif;color:var(--ink)}

  .sheet{position:absolute;width:660px;height:467px;background:var(--paper);overflow:hidden;box-shadow:0 10px 30px rgba(0,0,0,.45)}
  .sheet--outside{left:40px;top:22px;background:radial-gradient(circle at 0 0,var(--lime-soft) 0,#f6f8e2 35%,var(--paper) 70%)}
  .sheet--inside{left:500px;top:511px;background:linear-gradient(180deg,var(--lime-soft) 0,var(--paper) 45%,var(--paper) 70%,var(--lime-soft) 100%)}

  .tag{display:inline-block;position:relative;font-family:"Montserrat",sans-serif;font-weight:700;font-size:14px;letter-spacing:.2px;color:var(--forest);
       background:linear-gradient(180deg,var(--lime-bright),var(--lime));padding:4px 14px 4px 10px;border-radius:3px 12px 3px 12px;
       box-shadow:2px 2px 0 var(--leaf)}
  .body-copy{font-size:9.4px;line-height:1.32;color:var(--ink)}
  .body-copy p+p{margin-top:9px}

  /* outside */
  .flap{position:absolute;left:20px;top:24px;width:210px}
  .flap .tag{margin-bottom:12px}
  .flap .body-copy{margin-bottom:14px}
  .cover-photo{position:absolute;left:0;top:0}
  .brand-badge{position:absolute;text-align:center}
  .brand-name{font-family:"Questrial",sans-serif;font-size:27px;line-height:.95;color:var(--leaf);text-align:left}
  .brand-cta{font-size:9.4px;line-height:1.25;margin-top:6px;text-align:left}
  .brand-phone{font-family:"Montserrat",sans-serif;font-weight:700;color:var(--phone);font-size:15px;line-height:1.1;text-align:left;margin-top:4px}
  .brand-phone span{color:var(--ink);font-size:13px}
  .brand-badge--circle{left:448px;top:180px;width:190px}
  .brand-badge--panel{left:258px;top:302px;width:170px}

  /* inside */
  .column{position:absolute;top:0;width:220px;height:467px;padding:14px 16px 0}
  .column+.column{border-left:1px dashed var(--rule)}
  .column .tag{margin:10px 0 9px}
  .column .photo{position:absolute;left:16px;bottom:18px;width:188px;height:112px}
  .c1{left:0}.c2{left:220px}.c3{left:440px}
</style>
</head>
<body>

<!-- Outside of the leaflet -->
<section class="sheet sheet--outside" aria-label="Leaflet outside">
  <svg class="cover-photo" width="660" height="467" viewBox="0 0 660 467">
    <defs>
      <linearGradient id="gardenTone" x1="0" y1="0" x2="0" y2="1">
        <stop offset="0" stop-color="#bfe0f2"/>
        <stop offset=".35" stop-color="#6f9a45"/>
        <stop offset=".7" stop-color="#3c5d25"/>
        <stop offset="1" stop-color="#5fa333"/>
      </linearGradient>
      <radialGradient id="badgeShade" cx=".5" cy=".5" r=".5">
        <stop offset=".82" stop-color="#ffffff"/>
        <stop offset="1" stop-color="#e4e4e4"/>
      </radialGradient>
    </defs>
    <path d="M222,0 H660 V170 C600,150 540,175 500,215 C450,262 360,272 300,240 C255,215 230,170 222,120 Z" fill="#d9d9d9" transform="translate(0,14)"/>
    <path d="M222,0 H660 V170 C600,150 540,175 500,215 C450,262 360,272 300,240 C255,215 230,170 222,120 Z" fill="url(#gardenTone)" role="img" aria-label="Photo of a timber garden room with glazed walls on a sunlit lawn among trees"/>
    <circle cx="545" cy="262" r="96" fill="url(#badgeShade)"/>
  </svg>

  <div class="flap">
    <h2 class="tag">QUALITY SERVICE</h2>
    <div class="body-copy">
      <p>The service we provide is an end to end solution encompassing the location, the environment, your specific needs for the purpose of the structure, materials that are sympathetic to the locality, the services required and how you envisage your space will look and feel.</p>
      <p>Our buildings are exceptional and unrivalled. We source the best quality timber and materials for every stage of our building process right down to the paint systems we use. To this end we are always in the market place ensuring that any improvements in products, techniques and components are implemented by us straight away. We employ skilled craftsmen and a well regarded installation team to finish your building to the very highest of our expected standards.</p>
    </div>
    <h2 class="tag">WHAT WE OFFER</h2>
    <div class="body-copy">
      <p>We acknowledge that each customer has individual requirements based on their specific needs and as such we are flexible in our approach to design and installation. We are happy to replicate an existing building from an illustration, picture or even a pencil drawing on a napkin.</p>
    </div>
  </div>

  <div class="brand-badge brand-badge--panel">
    <div class="brand-name">Corrick<br>Yard<br>Buildings</div>
    <p class="brand-cta">Contact us for a no obligation consultation to see how we can make your vision become a reality.</p>
    <p class="brand-phone">01632 960418 <span>or</span><br>07700 900372</p>
  </div>

  <div class="brand-badge brand-badge--circle">
    <div class="brand-name">Corrick<br>Yard<br>Buildings</div>
    <p class="brand-cta">Contact us for a no obligation consultation to see how we can make your vision become a reality.</p>
    <p class="brand-phone">01632 960418 <span>or</span><br>07700 900372</p>
  </div>
</section>

<!-- Inside of the leaflet -->
<section class="sheet sheet--inside" aria-label="Leaflet inside">
  <div class="column c1">
    <div class="body-copy">
      <p>We design and build garden offices, studios, playrooms, garage workshops, therapy rooms and extra living accommodation.</p>
      <p>Corrick's is a local business that has been serving the East Hampshire community for almost 20 years. Over this time we have built a reputation for quality construction with customer satisfaction the overriding driving force.</p>
      <p>In recent years we've seen a huge increase in people working from home at least one day per week and a shift back to family focused lifestyles. Even large multi national companies are promoting home working as it has been shown by recent studies that home</p>
    </div>
    <svg class="photo" viewBox="0 0 188 112" role="img" aria-label="Photo of a grey contemporary garden studio with yellow chairs on a patio">
      <defs><linearGradient id="studioTone" x1="0" y1="0" x2="0" y2="1"><stop offset="0" stop-color="#d6dde2"/><stop offset=".55" stop-color="#6f7a82"/><stop offset="1" stop-color="#8a8f7a"/></linearGradient></defs>
      <rect width="188" height="112" fill="url(#studioTone)"/>
    </svg>
  </div>

  <div class="column c2">
    <div class="body-copy">
      <p>workers are more productive than solely office based employees. Corrick Yard Buildings is a greener way of working, improves work-life balance and accelerates your productivity.</p>
    </div>
    <h2 class="tag">OUR SERVICE</h2>
    <div class="body-copy">
      <p>Corrick Yard Buildings are totally bespoke, we will design and build your space in full consultation with you at every stage.</p>
      <p>Your garden room is intended as an extra room to use year round, for complete outdoor living, a hobby or relaxation room or simply as added space.</p>
      <p>We are proud to acknowledge that much of our trade is built around our reputation. We firmly believe that</p>
    </div>
    <svg class="photo" viewBox="0 0 188 112" role="img" aria-label="Photo of a garden room interior with a desk, laptop and plants">
      <defs><linearGradient id="officeTone" x1="0" y1="0" x2="0" y2="1"><stop offset="0" stop-color="#7d8f63"/><stop offset=".5" stop-color="#4b4a3c"/><stop offset="1" stop-color="#2c2620"/></linearGradient></defs>
      <rect width="188" height="112" fill="url(#officeTone)"/>
    </svg>
  </div>

  <div class="column c3">
    <div class="body-copy">
      <p>this is because we provide a personal service from design stage to installation and ongoing maintenance, where the customer always comes first and we leave them delighted with their building for years to come.</p>
    </div>
    <h2 class="tag">WHAT WE DO</h2>
    <div class="body-copy">
      <p>We'll visit your location to discuss your wants and needs, giving advice on what is possible within the existing regulations in your area. We will present a solution based on our conversation and work with you to enhance that design, finalise the design and agree a timescale for construction. Our service also includes assistance with any necessary planning permissions and on-site assembly, connection to services and only sign off the completed room once you are happy with every detail.</p>
    </div>
    <svg class="photo" viewBox="0 0 188 112" role="img" aria-label="Photo of a glazed garden office beside flowering shrubs under blue sky">
      <defs><linearGradient id="glazedTone" x1="0" y1="0" x2="0" y2="1"><stop offset="0" stop-color="#3f8fd6"/><stop offset=".45" stop-color="#5d7f3c"/><stop offset="1" stop-color="#6fae35"/></linearGradient></defs>
      <rect width="188" height="112" fill="url(#glazedTone)"/>
    </svg>
  </div>
</section>

</body>
</html>
```